Corvane Large Loss Tradeshow Booth Design

We need a tradeshow booth design for a 10x20 booth. We are a COMMERCIAL ONLY disaster restoration company focusing on water and flood restoration, fire and smoke remediation, mold and biohazard, structural repair and asset protection.

These are the links to the booth we need graphics designed for. The spec sheets for them are also in the attachments.
https://www.expostallden.com/Pelmora-Radial-Swift-Truss-p/pelmora.htm?CartID=2
https://www.expostallden.com/Tidecrest-39-Counter-p/tdc-39.htm?CartID=1
https://www.expostallden.com/6ft-Stretch-Table-Cover-p/tbl-6-stretch.htm?CartID=5

Target Market(s)

Real Estate, Educational Facilities, Hospitality Facilities, Medical Facilities

Industry/Entity Type

Construction

Requirements
Must have
• Our logo. The colors from the attached presentation. Pictures of COMMERCIAL ONLY facilities and losses (can use some from attached presentation). Our services (water and flood, fire and smoke, mold and biohazard, structural repair, asset protection). Our slogan (Exceeding your expectations when you need it most).
Nice to have
• Include the above
Should not have
• Do not include anything residential looking at all (no pictures). Do not include the case studies on the pictures.

```html
<!DOCTYPE html>
<html lang="en">
<head>
<meta charset="utf-8">
<title>Corvane Large Loss – Tradeshow Booth Graphics</title>
<link rel="stylesheet" href="https://fonts.googleapis.com/css2?family=Raleway:wght@300;400;500;700;800&display=swap">
<style>
  :root {
    --stage: #15172a;
    --teal: #3f6878;
    --orange: #f47b2a;
    --white: #ffffff;
    --light-grey: #e3e3e3;
    --ink-teal: #3f6878;
  }
  * { box-sizing: border-box; margin: 0; padding: 0; }
  html, body { width: 1200px; height: 560px; overflow: hidden; background: var(--stage); }
  body { font-family: "Raleway", Arial, sans-serif; position: relative; }

  .booth-panel { position: absolute; top: 90px; height: 380px; overflow: hidden; }
  .banner { background: var(--white); }
  .column { background: var(--teal); color: var(--white); }

  /* Banner parts */
  .brand {
    position: absolute; top: 10px; left: 0; right: 0;
    text-align: center; color: var(--orange); font-weight: 800; line-height: 1;
  }
  .brand-name { display: block; font-size: 22px; letter-spacing: 1px; }
  .brand-sub { display: block; font-size: 6.5px; letter-spacing: 0.6px; margin-top: 3px; }
  .header-cut { position: absolute; top: 45px; left: 0; width: 100%; height: 62px; }
  .photo { position: absolute; top: 106px; left: 0; width: 100%; height: 178px; }
  .accent-band { position: absolute; top: 284px; left: 0; width: 100%; height: 13px; background: var(--orange); }
  .site-url {
    position: absolute; left: 0; right: 0; text-align: center;
    font-size: 10px; font-weight: 400;
  }
  .banner .site-url { top: 346px; color: var(--ink-teal); }
  .column .site-url.top { top: 6px; color: var(--white); }
  .column .site-url.bottom { top: 347px; color: var(--white); }
  .dots { position: absolute; top: 361px; left: 50%; transform: translateX(-50%); display: flex; gap: 4px; }
  .dots span { width: 18px; height: 3px; }
  .dots .d1 { background: var(--teal); }
  .dots .d2 { background: var(--light-grey); }
  .dots .d3 { background: var(--orange); }

  /* Slogan */
  .slogan { position: absolute; top: 154px; left: 15px; width: 88px; height: 76px; }
  .slogan-frame {
    position: absolute; top: 6px; left: 0; width: 88px; height: 58px;
    border: 1px solid var(--orange); border-radius: 2px;
  }
  .quote-mark {
    position: absolute; color: var(--orange); font-weight: 800; font-size: 30px; line-height: 24px;
    height: 18px; overflow: hidden; background: var(--teal); padding: 0 2px;
  }
  .quote-mark.open { top: -4px; left: 3px; }
  .quote-mark.close { top: 58px; right: 3px; }
  .slogan-text { position: absolute; top: 16px; left: 0; width: 88px; text-align: center; }
  .slogan-text .lead { display: block; font-size: 6px; font-weight: 400; line-height: 8px; }
  .slogan-text .key { display: block; font-size: 10px; font-weight: 700; letter-spacing: 0.2px; line-height: 11px; }
  .slogan-text .tail {
    display: inline-block; background: var(--white); color: var(--teal);
    font-size: 5.5px; font-weight: 700; line-height: 7px; padding: 1px 4px; border-radius: 2px;
    white-space: nowrap;
  }

  /* Services */
  .services-heading {
    position: absolute; top: 11px; left: 8px; width: 101px; height: 107px;
    border: 1px solid var(--orange);
  }
  .services-heading h2 {
    position: absolute; left: 8px; top: 66px; color: var(--orange);
    font-size: 14px; line-height: 1.15; font-weight: 300;
  }
  .services-heading h2 strong { display: block; font-weight: 700; }
  .service-list { position: absolute; top: 144px; left: 10px; right: 4px; list-style: none; }
  .service-list li {
    position: relative; padding-left: 10px; font-size: 7.2px; font-weight: 700;
    line-height: 1.45; text-transform: uppercase; margin-bottom: 10px;
  }
  .service-list li::before {
    content: ""; position: absolute; left: 0; top: 2px; width: 5px; height: 5px;
    background: var(--orange);
  }
</style>
</head>
<body>

<!-- Banner 1 -->
<section class="booth-panel banner" style="left:35px;width:174px;">
  <div class="brand"><span class="brand-name">CORVANE</span><span class="brand-sub">RESTORATION SERVICES</span></div>
  <div class="photo" role="img" aria-label="Crew in protective suits inside a damaged commercial interior" style="background:linear-gradient(160deg,#6f776c,#a7a596 55%,#8a6b55);"></div>
  <svg class="header-cut" viewBox="0 0 100 60" preserveAspectRatio="none" aria-hidden="true">
    <polygon points="0,0 45,22 100,0 100,60 0,60" fill="var(--teal)"/>
    <polygon points="0,43 100,14 100,19 0,48" fill="var(--light-grey)"/>
    <polygon points="0,48 100,19 100,25 0,54" fill="var(--orange)"/>
    <polygon points="0,54 100,25 100,60 0,60" fill="#6f776c"/>
  </svg>
  <div class="accent-band"></div>
  <p class="site-url">corvanerestoration.com</p>
  <div class="dots"><span class="d1"></span><span class="d2"></span><span class="d3"></span></div>
</section>

<!-- Column 1 -->
<section class="booth-panel column" style="left:214px;width:118px;">
  <p class="site-url top">corvanerestoration.com</p>
  <div class="slogan">
    <div class="slogan-frame"></div>
    <span class="quote-mark open">&ldquo;</span>
    <div class="slogan-text">
      <span class="lead">Exceeding your</span>
      <span class="key">EXPECTATIONS</span>
      <span class="tail">when you need it most.</span>
    </div>
    <span class="quote-mark close">&rdquo;</span>
  </div>
</section>

<!-- Banner 2 -->
<section class="booth-panel banner" style="left:338px;width:196px;">
  <div class="brand"><span class="brand-name">CORVANE</span><span class="brand-sub">RESTORATION SERVICES</span></div>
  <div class="photo" role="img" aria-label="Flooded downtown street with office towers" style="background:linear-gradient(180deg,#9aa0a5,#6b7277 50%,#3f4447);"></div>
  <svg class="header-cut" viewBox="0 0 100 60" preserveAspectRatio="none" aria-hidden="true">
    <polygon points="0,0 45,22 100,0 100,60 0,60" fill="var(--teal)"/>
    <polygon points="0,43 100,14 100,19 0,48" fill="var(--light-grey)"/>
    <polygon points="0,48 100,19 100,25 0,54" fill="var(--orange)"/>
    <polygon points="0,54 100,25 100,60 0,60" fill="#9aa0a5"/>
  </svg>
  <div class="accent-band"></div>
  <p class="site-url">corvanerestoration.com</p>
  <div class="dots"><span class="d1"></span><span class="d2"></span><span class="d3"></span></div>
</section>

<!-- Services column -->
<section class="booth-panel column" style="left:541px;width:117px;">
  <div class="services-heading"><h2>OUR<strong>SERVICES</strong></h2></div>
  <ul class="service-list">
    <li>Water and Flood Restoration</li>
    <li>Fire and Smoke Restoration</li>
    <li>Mold Remediation</li>
    <li>Structural Repair</li>
    <li>Asset Management</li>
  </ul>
  <p class="site-url bottom">corvanerestoration.com</p>
</section>

<!-- Banner 3 -->
<section class="booth-panel banner" style="left:666px;width:196px;">
  <div class="brand"><span class="brand-name">CORVANE</span><span class="brand-sub">RESTORATION SERVICES</span></div>
  <div class="photo" role="img" aria-label="Water-buckled hardwood floor in a school gymnasium" style="background:linear-gradient(170deg,#d9dde2,#b58b5e 45%,#9a7048);"></div>
  <svg class="header-cut" viewBox="0 0 100 60" preserveAspectRatio="none" aria-hidden="true">
    <polygon points="0,0 55,22 100,0 100,60 0,60" fill="var(--teal)"/>
    <polygon points="0,14 100,43 100,48 0,19" fill="var(--light-grey)"/>
    <polygon points="0,19 100,48 100,54 0,25" fill="var(--orange)"/>
    <polygon points="0,25 100,54 100,60 0,60" fill="#d9dde2"/>
  </svg>
  <div class="accent-band"></div>
  <p class="site-url">corvanerestoration.com</p>
  <div class="dots"><span class="d1"></span><span class="d2"></span><span class="d3"></span></div>
</section>

<!-- Column 2 -->
<section class="booth-panel column" style="left:868px;width:117px;">
  <p class="site-url top">corvanerestoration.com</p>
  <div class="slogan">
    <div class="slogan-frame"></div>
    <span class="quote-mark open">&ldquo;</span>
    <div class="slogan-text">
      <span class="lead">Exceeding your</span>
      <span class="key">EXPECTATIONS</span>
      <span class="tail">when you need it most.</span>
    </div>
    <span class="quote-mark close">&rdquo;</span>
  </div>
</section>

<!-- Banner 4 -->
<section class="booth-panel banner" style="left:992px;width:174px;">
  <div class="brand"><span class="brand-name">CORVANE</span><span class="brand-sub">RESTORATION SERVICES</span></div>
  <div class="photo" role="img" aria-label="Fire-damaged steel roof structure of a commercial building" style="background:linear-gradient(180deg,#c9c9c9,#7d7d7d 50%,#3a3634);"></div>
  <svg class="header-cut" viewBox="0 0 100 60" preserveAspectRatio="none" aria-hidden="true">
    <polygon points="0,0 55,22 100,0 100,60 0,60" fill="var(--teal)"/>
    <polygon points="0,14 100,43 100,48 0,19" fill="var(--light-grey)"/>
    <polygon points="0,19 100,48 100,54 0,25" fill="var(--orange)"/>
    <polygon points="0,25 100,54 100,60 0,60" fill="#c9c9c9"/>
  </svg>
  <div class="accent-band"></div>
  <p class="site-url">corvanerestoration.com</p>
  <div class="dots"><span class="d1"></span><span class="d2"></span><span class="d3"></span></div>
</section>

</body>
</html>
```